designing a website for a vacation beach house rental

We are buying a vacation rental on an awesome beach on the Isle of Palms in South Carolina. The closing is not until November 30 so we will only have the photos from the current home and we can change the photos once we move our furniture in. We want the website to be exciting and interactive and for people to be able to go to a facebook page (that needs to be created) and the name of the beach house needs to be created (the address is 47 Tidewater Lane, Isle of Palms. We need to be able to take this site and add it to STYX and NookSpot and Bay Q&T and other travel sites. We need the person that clicks on it to be hooked from the first second. We think this one is pretty good but we want ours way better http://driftwoodcovehouse.example/ The price per week will be $7200 so the website needs to be elegant, stunning, all inclusive, retreat, relaxing, friends and family, eating together, amazing food town, beaches, golf, cocktails, wine, restaurants, history, architecture, opulence, Look up Charleston, SC to get an idea of what the area is all about. Top Chefs and top wines.

Target Market(s)

Upper class families with children; classy dressing; golfers; foodies; wine lovers; in shaper beach goers living the dream of a gorgeous beach house with friends and family at the pool, eating together, beach together, cooking together, playing games, walking on the beach, running on the beach, watching the sunset on the beach

Industry/Entity Type

House

Logo Text

the look and feel of an upper class family on vacation in an exclusive resort

Number of Pages Required

5+ page

Font styles to use
Serif

Requirements
Must have
• Lots of photos and movement; easy for me to update is a MUST; easy for a guest to register for staying; a calendar that will update automatically when someone pays; ability to take credit cards and CoinLoop; guest book; keep up with the number of visits; all of the bells and whistles of the most modern websites; also works on any device like ZPhone or ZSlate or any smartphone

```html
<!DOCTYPE html>
<html lang="en">
<head>
<meta charset="utf-8">
<title>Seabright Manor Beach House — Isle of Palms</title>
<link rel="stylesheet" href="https://fonts.googleapis.com/css2?family=Arimo:wght@400;700&family=Open+Sans:ital,wght@0,300;0,400;1,400&display=swap">
<style>
:root{
  --accent:#f6a400;
  --ink:#111111;
  --muted:#a9a9a9;
  --text:#555555;
  --white:#ffffff;
  --night:#0b0b12;
  --footer:#0a0a0a;
  --panel:rgba(12,12,16,.82);
  --line:#cfcfcf;
}
*{margin:0;padding:0;box-sizing:border-box}
html,body{width:1200px;height:3186px;overflow:hidden;background:var(--white)}
body{position:relative;font-family:"Arimo",Helvetica,Arial,sans-serif;color:var(--ink)}
.abs{position:absolute}
.center{transform:translateX(-50%);text-align:center;white-space:nowrap}

/* hero */
.hero{left:0;top:0;width:1200px;height:675px;
  background:linear-gradient(180deg,#1d1a3e 0%,#4d3f86 22%,#a56aa6 40%,#d28aa2 48%,#2c2846 60%,#151626 78%,#0c0c14 100%)}
.topbar{left:0;top:0;width:1200px;height:49px;background:rgba(5,5,10,.85)}
.brand-mini{left:22px;top:12px;display:flex;align-items:center;gap:8px;color:var(--accent);font-weight:700;font-size:16px}
.brand-mini .dot{width:20px;height:20px;border-radius:50%;background:var(--accent)}
.nav a{position:absolute;top:17px;color:var(--white);font-size:13px;text-decoration:none}
.btn-book{left:1096px;top:10px;width:88px;height:28px;border-radius:14px;background:var(--accent);color:var(--white);font-size:13px;font-weight:700;line-height:28px;text-align:center}
.logo{left:600px;top:96px;color:var(--white);font-size:30px;font-weight:400;letter-spacing:.5px}
.logo-sub{left:600px;top:136px;color:var(--white);font-size:8px;letter-spacing:2px}

.booking{left:282px;top:170px;width:636px;height:365px;background:var(--panel);border:1px solid #333;border-radius:8px}
.booking-title{left:600px;top:191px;color:var(--white);font-size:12px;letter-spacing:.3px}
.card{left:323px;top:219px;width:556px;height:278px;background:var(--white);border-radius:6px}
.field-label{font-size:13px;color:#222}
.sel{width:42px;height:20px;border:1px solid var(--line);font-size:12px;line-height:18px;padding-left:8px}
.sel::after{content:"";position:absolute;right:0;top:0;width:16px;height:18px;background:var(--accent)}
.input{left:348px;width:325px;border-bottom:1px solid #9a9a9a;font-size:12px;color:#555;padding-bottom:8px}
.input.active{border-bottom:2px solid var(--accent);color:var(--accent);font-size:10px}
.tiny{font-size:7px;color:#888}
.promo{left:684px;top:236px;width:183px;height:248px;
  background:linear-gradient(160deg,#5fb6dc 0%,#bfe2ef 45%,#e8d6c4 70%,#c9a488 100%)}
.promo-title{left:776px;top:252px;color:var(--white);font-size:18px}
.promo-sub{left:776px;top:274px;color:var(--white);font-size:7px}
.promo-btn{left:737px;top:295px;width:62px;height:16px;border:1px solid var(--white);border-radius:8px;background:#3a9fd0;color:var(--white);font-size:6px;line-height:14px;text-align:center}
.calc{left:600px;top:508px;color:var(--white);font-size:11px}
.days{left:765px;top:506px;color:var(--white);font-size:11px}
.days b{color:var(--accent);font-weight:400}
.ghost-btn{width:86px;height:26px;border:1.5px solid var(--white);border-radius:13px;color:var(--white);font-size:11px;line-height:23px;text-align:center}
.hero-link{top:636px;color:var(--white);font-size:14px}
.hero-link span{color:var(--accent)}

/* how to book */
.section-title{left:600px;font-size:28px;font-weight:400;color:#222;letter-spacing:.2px}
.section-title b{font-weight:700}
.step{width:180px;text-align:center;transform:translateX(-50%)}
.step svg{display:block;margin:0 auto}
.step p{margin-top:20px;font-size:13px;color:#c2c2c2}
.step.current p{color:var(--ink);font-size:16px;margin-top:14px}

/* media bands */
.band{left:0;width:1200px}
.video-band{top:977px;height:482px;background:linear-gradient(180deg,#d8cfc6 0%,#bba38c 35%,#8b6a4d 55%,#c9baa6 75%,#ece4d9 100%)}
.under-band{top:1965px;height:484px;background:radial-gradient(ellipse at 55% 40%,#4fb8c4 0%,#1f7f92 45%,#0c4a5e 100%)}
.sunset-band{top:2710px;height:310px;background:linear-gradient(180deg,#fff3a6 0%,#ffcf3a 30%,#f7a10e 60%,#c66a08 82%,#4a2a10 100%)}
.arrow{width:34px;height:34px;border-radius:50%;background:rgba(20,20,20,.7)}
.dots{display:flex;gap:6px;transform:translateX(-50%)}
.dots i{width:6px;height:6px;border-radius:50%;background:rgba(255,255,255,.8)}
.dots i:first-child{background:var(--white);width:7px;height:7px}
.dots.light i{background:#d7d7d7}
.dots.light i:first-child{background:var(--accent)}
.video-title{left:600px;top:1250px;color:var(--white);font-size:30px}
.video-copy{left:600px;color:var(--white);font-family:"Open Sans",Arial,sans-serif;font-style:italic;font-size:14px}

/* counters */
.stat{transform:translateX(-50%);text-align:center}
.stat strong{display:block;font-size:88px;font-weight:400;line-height:1;letter-spacing:-2px}
.stat span{display:block;margin-top:14px;font-size:17px}
.stat.hl strong,.stat.hl span{color:var(--accent)}

/* testimonial */
.quote{left:600px;top:2520px;width:760px;transform:translateX(-50%);text-align:center;font-family:"Open Sans",Arial,sans-serif;font-weight:300;font-size:14.5px;line-height:22px;color:var(--text)}
.quote-by{left:600px;top:2616px;font-size:15px;color:#222}

/* footer */
.footer{left:0;top:3020px;width:1200px;height:166px;background:var(--footer);color:#bdbdbd;font-size:10px}
.footer h4{position:absolute;font-size:10px;color:var(--white);font-weight:700}
.footer p{position:absolute;line-height:12px}
.copy{left:600px;top:3168px;font-size:7px;color:#8a8a8a}
.social{width:16px;height:16px;border-radius:50%;background:#cfcfcf}
.to-top{left:1166px;top:2950px;width:18px;height:22px;border-radius:3px;background:rgba(40,40,40,.85)}
</style>
</head>
<body>

<!-- hero -->
<section class="abs hero" role="img" aria-label="Sunset over the ocean in purple and pink tones with a dock on the water"></section>
<header class="abs topbar">
  <div class="abs brand-mini"><span class="dot"></span>Seabright</div>
  <nav class="nav">
    <a style="left:701px">Home</a>
    <a style="left:802px">About</a>
    <a style="left:888px">Things to Do</a>
    <a style="left:1003px">Contact Us</a>
  </nav>
  <div class="abs btn-book">Book Now</div>
</header>
<div class="abs center logo">Seabright Manor</div>
<div class="abs center logo-sub">BEACH HOUSE</div>

<div class="abs booking"></div>
<div class="abs center booking-title">FILL YOUR BOOKING DETAILS</div>
<div class="abs card"></div>
<div class="abs field-label" style="left:348px;top:240px">Adult</div>
<div class="abs sel" style="left:423px;top:236px">5</div>
<div class="abs field-label" style="left:553px;top:240px">Children</div>
<div class="abs sel" style="left:629px;top:236px">8</div>
<div class="abs tiny" style="left:590px;top:260px">Maximum Occupancy - 16</div>
<div class="abs input active" style="top:266px">First Name</div>
<div class="abs input" style="top:316px">Last Name</div>
<div class="abs input" style="top:358px">Email</div>
<div class="abs tiny" style="left:530px;top:381px">Booking details will be sent to this mail</div>
<div class="abs input" style="top:398px">Phone No</div>
<div class="abs field-label" style="left:348px;top:458px;font-size:11px">Pre-Payment Required *</div>
<div class="abs tiny" style="left:348px;top:474px">There is a 50.00% total payment required to book this home.</div>
<div class="abs promo" role="img" aria-label="Guest relaxing on a porch swing by the sea"></div>
<div class="abs center promo-title">COME &amp; ENJOY</div>
<div class="abs center promo-sub">The Beauty of Isle of Palms</div>
<div class="abs promo-btn">BOOK NOW</div>
<div class="abs center calc">CALCULATE YOUR STAY</div>
<div class="abs days">No of Days Selected : <b>7</b></div>
<div class="abs ghost-btn" style="left:287px;top:556px">BACK</div>
<div class="abs ghost-btn" style="left:832px;top:556px">NEXT</div>
<svg class="abs" style="left:591px;top:600px" width="20" height="32" viewBox="0 0 20 32" aria-hidden="true">
  <rect x="1" y="1" width="18" height="30" rx="9" fill="none" stroke="#fff" stroke-width="1.5"/>
  <line x1="10" y1="7" x2="10" y2="13" stroke="#fff" stroke-width="1.5"/>
</svg>
<div class="abs hero-link" style="left:30px">How to Book? <span>Click Here</span></div>
<div class="abs hero-link" style="right:21px">Any Questions? <span>Contact Us</span></div>

<!-- how to book -->
<h2 class="abs center section-title" style="top:690px">HOW TO <span style="font-weight:400">BOOK</span></h2>
<div class="abs step current" style="left:238px;top:795px">
  <svg width="66" height="58" viewBox="0 0 66 58" aria-hidden="true">
    <rect x="2" y="6" width="56" height="46" rx="3" fill="none" stroke="#f6a400" stroke-width="3"/>
    <rect x="2" y="6" width="56" height="10" fill="#f6a400"/>
    <line x1="14" y1="2" x2="14" y2="10" stroke="#f6a400" stroke-width="3"/>
    <line x1="46" y1="2" x2="46" y2="10" stroke="#f6a400" stroke-width="3"/>
    <g fill="#f6a400"><rect x="9" y="22" width="8" height="6"/><rect x="21" y="22" width="8" height="6"/><rect x="33" y="22" width="8" height="6"/><rect x="45" y="22" width="8" height="6"/><rect x="9" y="32" width="8" height="6"/><rect x="21" y="32" width="8" height="6"/><rect x="33" y="32" width="8" height="6"/><rect x="45" y="32" width="8" height="6"/><rect x="9" y="42" width="8" height="6"/><rect x="21" y="42" width="8" height="6"/></g>
    <path d="M58 44 l4 10 2-4 4 4" fill="none" stroke="#333" stroke-width="2"/>
  </svg>
  <p>Select Check-in Date</p>
</div>
<div class="abs step" style="left:446px;top:800px">
  <svg width="52" height="42" viewBox="0 0 52 42" aria-hidden="true">
    <rect x="2" y="4" width="48" height="36" rx="2" fill="none" stroke="#bdbdbd" stroke-width="2"/>
    <line x1="2" y1="12" x2="50" y2="12" stroke="#bdbdbd" stroke-width="2"/>
    <g fill="#cfcfcf"><rect x="8" y="17" width="7" height="5"/><rect x="18" y="17" width="7" height="5"/><rect x="28" y="17" width="7" height="5"/><rect x="38" y="17" width="7" height="5"/><rect x="8" y="26" width="7" height="5"/><rect x="18" y="26" width="7" height="5"/><rect x="28" y="26" width="7" height="5"/></g>
  </svg>
  <p>Select Check-out Date</p>
</div>
<div class="abs step" style="left:650px;top:800px">
  <svg width="52" height="42" viewBox="0 0 52 42" aria-hidden="true" fill="none" stroke="#bdbdbd" stroke-width="2">
    <circle cx="17" cy="12" r="7"/><circle cx="35" cy="12" r="7"/>
    <path d="M3 38 c0-10 6-15 14-15 s14 5 14 15z"/><path d="M21 38 c0-10 6-15 14-15 s14 5 14 15z"/>
  </svg>
  <p>No of Occupancy</p>
</div>
<div class="abs step" style="left:843px;top:800px">
  <svg width="56" height="42" viewBox="0 0 56 42" aria-hidden="true" fill="none" stroke="#bdbdbd" stroke-width="2">
    <rect x="2" y="2" width="52" height="38" rx="3"/>
    <rect x="9" y="10" width="14" height="16"/>
    <line x1="29" y1="12" x2="47" y2="12"/><line x1="29" y1="19" x2="47" y2="19"/><line x1="29" y1="26" x2="42" y2="26"/><line x1="9" y1="33" x2="47" y2="33"/>
  </svg>
  <p>Fill your Details</p>
</div>
<div class="abs step" style="left:1009px;top:798px">
  <svg width="36" height="44" viewBox="0 0 36 44" aria-hidden="true" fill="none" stroke="#bdbdbd" stroke-width="2">
    <path d="M8 20 v-8 a10 10 0 0 1 20 0 v8"/><rect x="3" y="20" width="30" height="22" rx="3"/><circle cx="18" cy="30" r="3"/>
  </svg>
  <p>Pay 50% to Confirm</p>
</div>

<!-- video band -->
<section class="abs band video-band" role="img" aria-label="Blurred photo of a person on the beach at golden sunset"></section>
<div class="abs arrow" style="left:38px;top:1198px"></div>
<svg class="abs" style="left:38px;top:1198px" width="34" height="34" aria-hidden="true"><path d="M19 11 l-6 6 6 6" fill="none" stroke="#fff" stroke-width="2"/></svg>
<div class="abs arrow" style="left:1130px;top:1198px"></div>
<svg class="abs" style="left:1130px;top:1198px" width="34" height="34" aria-hidden="true"><path d="M15 11 l6 6 -6 6" fill="none" stroke="#fff" stroke-width="2"/></svg>
<svg class="abs" style="left:557px;top:1141px" width="84" height="84" aria-hidden="true">
  <circle cx="42" cy="42" r="39" fill="rgba(255,255,255,.15)" stroke="#fff" stroke-width="4"/>
  <path d="M34 26 l24 16 -24 16z" fill="#fff"/>
</svg>
<div class="abs center video-title">WATCH VIDEOS</div>
<div class="abs center video-copy" style="top:1296px">Have a quick look of Seabright Manor Beach House.</div>
<div class="abs center video-copy" style="top:1317px">We have a covered deck here you can have wine, tea and you can watch the sun set from the house.</div>
<div class="abs dots" style="left:600px;top:1437px"><i></i><i></i><i></i><i></i><i></i></div>

<!-- counters -->
<h2 class="abs center section-title" style="top:1484px">TOTAL NO OF <b>VISITS</b></h2>
<div class="abs stat hl" style="left:238px;top:1650px"><strong>78</strong><span>VISITS</span></div>
<div class="abs stat" style="left:478px;top:1650px"><strong>125</strong><span>PEOPLES</span></div>
<div class="abs stat" style="left:720px;top:1650px"><strong>35</strong><span>FAMILIES</span></div>
<div class="abs stat" style="left:966px;top:1650px"><strong>18</strong><span>COUPLES</span></div>

<!-- underwater band -->
<section class="abs band under-band" role="img" aria-label="Swimmer with fins underwater in clear turquoise sea"></section>
<div class="abs arrow" style="left:38px;top:2190px"></div>
<svg class="abs" style="left:38px;top:2190px" width="34" height="34" aria-hidden="true"><path d="M19 11 l-6 6 6 6" fill="none" stroke="#fff" stroke-width="2"/></svg>
<div class="abs arrow" style="left:1130px;top:2190px"></div>
<svg class="abs" style="left:1130px;top:2190px" width="34" height="34" aria-hidden="true"><path d="M15 11 l6 6 -6 6" fill="none" stroke="#fff" stroke-width="2"/></svg>
<div class="abs dots" style="left:600px;top:2426px"><i></i><i></i><i></i><i></i><i></i></div>

<!-- testimonial -->
<blockquote class="abs quote">“Where to begin? Everything about this condo was lovely. The location, the owners, the home itself. Everything was in top repair, spotless and current. We were delighted with it all. The description of the home was entirely accurate but it was even in person.”</blockquote>
<div class="abs center quote-by">Guest, Brazil</div>
<div class="abs dots light" style="left:600px;top:2690px"><i></i><i></i><i></i><i></i><i></i></div>

<!-- sunset band -->
<section class="abs band sunset-band" role="img" aria-label="Silhouette of a person kicking a ball on the beach at sunset"></section>
<div class="abs to-top"></div>
<svg class="abs" style="left:1166px;top:2950px" width="18" height="22" aria-hidden="true"><path d="M5 13 l4-4 4 4" fill="none" stroke="#fff" stroke-width="1.5"/></svg>
<div class="abs social" style="left:1145px;top:2995px"></div>
<div class="abs social" style="left:1169px;top:2995px"></div>

<!-- footer -->
<footer class="abs footer">
  <h4 style="left:110px;top:20px">ADDRESS</h4>
  <p style="left:110px;top:44px">47 Tidewater Lane,<br>Isle of Palms, SC 29451.</p>
  <p style="left:110px;top:84px">Owner Name</p>
  <p style="left:110px;top:106px">+00 55501 0199</p>

  <h4 style="left:408px;top:20px">CATEGORIES</h4>
  <p style="left:408px;top:44px;line-height:22px">Beach<br>Charleston<br>Food<br>Golf</p>
  <p style="left:512px;top:44px;line-height:22px">History<br>Holidays<br>How To<br>Isle of Palms</p>
  <p style="left:620px;top:44px;line-height:22px">Local Information<br>News<br>News Letter<br>Our Guest Book</p>
  <p style="left:735px;top:44px;line-height:22px">South Carolina<br>Tours<br>Vacational Rental<br>Videos</p>

  <h4 style="left:1032px;top:20px">PAGES</h4>
  <p style="left:1032px;top:44px;line-height:22px">Home<br>About<br>Things to Do<br>Contact Us</p>
</footer>
<div class="abs center copy">© Copyright - Seabright Manor Beach House Isle of Palms, South Carolina</div>

</body>
</html>
```